Quillmont Renovations Letterhead

Quillmont does not do actual renovation, but rather handles high end project management of renovation (primarily residential with an eye toward commercial and International) The renovation work could look very different between projects. This company works directly with the clients and manages the work of contractors, architects and interior designers (either subcontracted directly by Quillmont or hired by the client and entrusted to Quillmont to manage). Clients are high end in the economic scale and all materials should speak to that audience. Provoke a sense of change, openness and imagination, trust and integrity. The owner is female, but the audience will be heavily slanted male. It should not be a "feminine" or "masculine" looking . If anything, slant more on the masculine side.

Clean, simple, yet creative and artistically appealing. The logo should be clear and not competing with too many surrounding design elements.

There is a contest also on for business card. Please check that section if you would like to compete for both.

Get your creative juices going!

Target Market(s)

High end cients. Additional audience: professionals (architects, etc...) designers, contractors

Industry/Entity Type

Residential

Requirements
Must have
• Logo must be included in all materials

```html
<!DOCTYPE html>
<html lang="en">
<head>
<meta charset="utf-8">
<title>Quillmont Renovations Letterhead</title>
<link href="https://fonts.googleapis.com/css2?family=Nunito+Sans:wght@400;700&display=swap" rel="stylesheet">
<style>
  :root {
    --charcoal: #3e3d40;
    --mist: #c2dedc;
    --teal: #1fa89b;
    --white: #ffffff;
  }
  * { margin: 0; padding: 0; box-sizing: border-box; }
  html, body {
    width: 927px;
    height: 1200px;
    overflow: hidden;
    background: var(--charcoal);
  }
  .letterhead {
    position: relative;
    width: 927px;
    height: 1200px;
    background: var(--charcoal);
    font-family: "Nunito Sans", Arial, sans-serif;
  }
  .letterhead__field {
    position: absolute;
    inset: 0;
  }
  .brand {
    position: absolute;
    left: 73px;
    top: 64px;
    width: 280px;
  }
  .brand__mark {
    display: block;
    width: 44px;
    height: 44px;
    margin: 0 0 34px 103px;
    background: var(--teal);
  }
  .brand__name {
    font-size: 19px;
    font-weight: 700;
    color: var(--white);
    letter-spacing: 0.01em;
    white-space: nowrap;
    text-transform: uppercase;
  }
  .contact {
    position: absolute;
    left: 73px;
    top: 194px;
    font-size: 13.5px;
    line-height: 20.5px;
    color: var(--teal);
    font-style: normal;
  }
  .footer {
    position: absolute;
    left: 0;
    bottom: 0;
    width: 927px;
    height: 73px;
    display: flex;
    align-items: center;
    justify-content: center;
  }
  .footer__web {
    font-size: 16px;
    color: var(--teal);
    letter-spacing: 0.36em;
    text-transform: uppercase;
    padding-left: 0.36em;
  }
</style>
</head>
<body>
  <div class="letterhead">
    <svg class="letterhead__field" width="927" height="1200" viewBox="0 0 927 1200" aria-hidden="true">
      <polygon points="689,65 927,65 927,1127 0,1127 0,439" fill="var(--mist)"/>
    </svg>

    <header class="brand">
      <span class="brand__mark" aria-hidden="true"></span>
      <div class="brand__name">Quillmont Renovations</div>
    </header>

    <address class="contact">
      <div>5678 Harbor Ln., Ste. 2</div>
      <div>Lakeview, USA 30451</div>
      <div>800.555.0142</div>
    </address>

    <footer class="footer">
      <span class="footer__web">quillmontrenovations.com</span>
    </footer>
  </div>
</body>
</html>
```